Email Signature

Our company is having its 10th anniversary in 2021. We would like a new email signature to celebrate the occasion. Attached is our business card design.
Please refer to our website for actual contact details.
www.tarvinestates.com.au

Industry/Entity Type

Real Estate

Requirements
Must have
• Our logo
Email
Contact Numbers
Address
Website address

Celebrating 10 years in 2021
Nice to have
• Something that blends the designs of our website and business card

```html
<!DOCTYPE html>
<html lang="en">
<head>
<meta charset="utf-8">
<title>Tarvine Estates – Email Signature</title>
<link rel="stylesheet" href="https://fonts.googleapis.com/css2?family=Montserrat:wght@800&family=Source+Sans+3:wght@400;600;700;900&display=swap">
<style>
  :root {
    --brand-blue: #1f5593;
    --brand-ink: #111111;
    --paper: #ffffff;
  }
  * { box-sizing: border-box; margin: 0; padding: 0; }
  html, body {
    width: 1124px;
    height: 1200px;
    overflow: hidden;
    background: var(--paper);
  }
  .signature {
    position: relative;
    width: 1124px;
    height: 1200px;
    background: var(--paper);
    font-family: "Source Sans 3", "Helvetica Neue", Arial, sans-serif;
  }
  .brand-square {
    position: absolute;
    left: 402px;
    top: 110px;
    width: 320px;
    height: 320px;
    background: var(--brand-blue);
  }
  .brand-name {
    position: absolute;
    left: 0;
    top: 484px;
    width: 100%;
    text-align: center;
    font-family: "Montserrat", Arial, sans-serif;
    font-weight: 800;
    font-size: 88px;
    letter-spacing: 2px;
    color: var(--brand-ink);
    line-height: 1;
  }
  .skyline {
    position: absolute;
    left: 0;
    top: 690px;
    width: 100%;
    height: 80px;
    background: linear-gradient(to bottom, rgba(31,85,147,0) 0%, rgba(31,85,147,0.55) 45%, var(--brand-blue) 100%);
  }
  .anniversary-band {
    position: absolute;
    left: 0;
    top: 768px;
    width: 100%;
    height: 432px;
    background: var(--brand-blue);
    color: var(--paper);
  }
  .celebrate {
    position: absolute;
    top: 138px;
    font-weight: 700;
    font-size: 54px;
    line-height: 1;
  }
  .celebrate--lead { left: 124px; }
  .celebrate--year { left: 750px; word-spacing: 14px; letter-spacing: 2px; }
  .milestone {
    position: absolute;
    left: 440px;
    top: 56px;
    width: 240px;
    height: 200px;
  }
  .milestone__number {
    position: absolute;
    left: 0;
    top: 0;
    width: 100%;
    text-align: center;
    font-weight: 900;
    font-size: 190px;
    line-height: 0.85;
    letter-spacing: -10px;
    color: var(--paper);
  }
  .milestone__label {
    position: absolute;
    left: 10px;
    top: 140px;
    width: 220px;
    height: 50px;
    background: var(--paper);
    color: var(--brand-blue);
    text-align: center;
    font-weight: 600;
    font-size: 30px;
    line-height: 50px;
    letter-spacing: 10px;
  }
  .contact {
    position: absolute;
    left: 0;
    width: 100%;
    text-align: center;
    line-height: 1;
  }
  .contact--web {
    top: 284px;
    font-weight: 700;
    font-size: 33px;
  }
  .contact--lines {
    top: 331px;
    font-weight: 400;
    font-size: 32px;
  }
  .contact--lines p + p { margin-top: 6px; }
</style>
</head>
<body>
  <main class="signature">
    <div class="brand-square" aria-hidden="true"></div>
    <h1 class="brand-name">TARVINE ESTATES</h1>

    <div class="skyline" role="img" aria-label="City skyline silhouette rising above the blue band"></div>

    <section class="anniversary-band">
      <p class="celebrate celebrate--lead">Celebrating</p>
      <div class="milestone">
        <span class="milestone__number">10</span>
        <span class="milestone__label">YEARS</span>
      </div>
      <p class="celebrate celebrate--year">in 2021.</p>

      <p class="contact contact--web">• www.tarvinestates.com.au •</p>
      <div class="contact contact--lines">
        <p>• 561-402-8817 • 561-409-2254 • info@tarvinestates.com •</p>
        <p>• 2240 s. Harbor Avenue #210 Coral Springs, Florida 33065 •</p>
      </div>
    </section>
  </main>
</body>
</html>
```